Report Cover

This is for a Binder Front, Side, Back. I have uploaded a few examples. We are an education resource company that delivers data in a format that allows districts to make better decisions. Our color palette is uploaded as well.

```html
<!DOCTYPE html>
<html lang="en">
<head>
<meta charset="utf-8">
<title>2024 Comprehensive Needs Assessment – Cedarbrook School District</title>
<link rel="stylesheet" href="https://fonts.googleapis.com/css2?family=Barlow:wght@500;700&display=swap">
<style>
  :root {
    --paper: #ffffff;
    --tone-yellow: #fdd52a;
    --tone-sage: #82ad94;
    --tone-lime: #84e10a;
    --tone-orange: #fd5636;
    --tone-purple: #8a58c4;
    --tone-teal: #4cf49a;
    --badge-blue: #3f7ff0;
    --badge-frame: #cfd3d6;
    --navy: #0a1890;
    --ink: #111111;
    --title-orange: #f54f1f;
    --title-purple: #8a22d6;
    --brand-green: #7fd11b;
  }
  html, body {
    margin: 0;
    padding: 0;
    width: 927px;
    height: 1200px;
    overflow: hidden;
    background: var(--paper);
  }
  .cover {
    position: relative;
    width: 927px;
    height: 1200px;
    overflow: hidden;
    background: var(--paper);
    font-family: "Barlow", "Helvetica Neue", Arial, sans-serif;
  }
  .backdrop {
    position: absolute;
    left: 0;
    top: 0;
  }
  .brand {
    position: absolute;
    left: 478px;
    top: 52px;
    display: flex;
    align-items: center;
    gap: 10px;
  }
  .brand-dot {
    width: 18px;
    height: 18px;
    border-radius: 50%;
    background: var(--brand-green);
  }
  .brand-name {
    font-weight: 500;
    font-size: 29px;
    line-height: 29px;
    color: #1b1b1b;
  }
  .year-badge {
    position: absolute;
    left: 436px;
    top: 207px;
    width: 309px;
    height: 125px;
    border-radius: 6px;
    background: var(--badge-frame);
  }
  .year-badge .face {
    position: absolute;
    left: 13px;
    top: 9px;
    width: 286px;
    height: 108px;
    border-radius: 6px;
    background: linear-gradient(180deg, #5a95f7 0%, var(--badge-blue) 60%, #2f6fe4 100%);
  }
  .headings {
    position: absolute;
    left: 0;
    top: 0;
  }
  .year { font-weight: 700; fill: #ffffff; }
  .report-kind { font-weight: 700; fill: var(--navy); }
  .report-name { font-weight: 500; fill: var(--ink); }
  .district-name { font-weight: 700; fill: var(--title-orange); }
  .district-type { font-weight: 500; fill: var(--title-purple); }
</style>
</head>
<body>
<main class="cover">
  <svg class="backdrop" width="927" height="1200" viewBox="0 0 927 1200">
    <defs>
      <linearGradient id="upper-tones" x1="0" y1="0" x2="0.6" y2="1">
        <stop offset="0" stop-color="var(--tone-yellow)" stop-opacity="0.28"/>
        <stop offset="0.35" stop-color="var(--tone-sage)" stop-opacity="0.3"/>
        <stop offset="0.6" stop-color="var(--tone-lime)" stop-opacity="0.22"/>
        <stop offset="1" stop-color="var(--tone-orange)" stop-opacity="0.26"/>
      </linearGradient>
      <linearGradient id="lower-tones" x1="0" y1="1" x2="1" y2="0">
        <stop offset="0" stop-color="var(--tone-teal)" stop-opacity="0.26"/>
        <stop offset="0.5" stop-color="var(--tone-yellow)" stop-opacity="0.24"/>
        <stop offset="1" stop-color="var(--tone-purple)" stop-opacity="0.24"/>
      </linearGradient>
    </defs>
    <path class="tone-field" role="img" aria-label="Decorative field of raised colour tiles in yellow, sage, lime, mint and orange"
          d="M0 0 H380 V200 L300 340 V490 L385 500 V630 L250 780 L100 830 H0 Z" fill="url(#upper-tones)"/>
    <path class="tone-field" role="img" aria-label="Decorative field of raised colour tiles in teal, yellow, sage and purple"
          d="M480 1200 V1090 L650 1045 L850 1010 H927 V1200 Z" fill="url(#lower-tones)"/>
  </svg>

  <div class="brand">
    <span class="brand-dot"></span>
    <span class="brand-name">Learning Ledger, LLC</span>
  </div>

  <div class="year-badge"><div class="face"></div></div>

  <svg class="headings" width="927" height="1200" viewBox="0 0 927 1200" aria-label="2024 Comprehensive Needs Assessment, Cedarbrook School District">
    <text class="year" x="462" y="318" font-size="132" textLength="264" lengthAdjust="spacingAndGlyphs">2024</text>
    <text class="report-kind" x="333" y="411" font-size="66" textLength="523" lengthAdjust="spacingAndGlyphs">COMPREHENSIVE</text>
    <text class="report-name" x="333" y="478" font-size="58" textLength="523" lengthAdjust="spacingAndGlyphs">NEEDS ASSESSMENT</text>
    <text class="district-name" x="76" y="918" font-size="131" textLength="776" lengthAdjust="spacingAndGlyphs">CEDARBROOK</text>
    <text class="district-type" x="78" y="1000" font-size="96" textLength="771" lengthAdjust="spacingAndGlyphs">SCHOOL DISTRICT</text>
  </svg>
</main>
</body>
</html>
```